Cover for CD-single

TOVA is a young singer-songwriter and needs a CD cover design for her first single "Stars over harbour". Her song is about her best friend who recently moved from Europe to Australia with her family. But even though they now live on the other side of the world, they will always be there for each other.
You can use the picture attached or you can see it as an inspiration.
Please put the name of the artist: TOVA
and the name of the song on the cover: Stars over harbour

```html
<!DOCTYPE html>
<html lang="en">
<head>
<meta charset="utf-8">
<title>TOVA – Stars over harbour</title>
<link rel="stylesheet" href="https://fonts.googleapis.com/css2?family=Kalam:wght@400&family=Gochi+Hand&display=swap">
<style>
  :root {
    --page: #ffffff;
    --board: #eeeff1;
    --paper-dark: #2f2f2f;
    --paper-mid: #444444;
    --card: #ffffff;
    --ink: #111111;
    --title: #ffffff;
    --heart: #b8662a;
    --tape: rgba(222, 196, 140, 0.82);
    --photo-light: #b4bcc3;
    --photo-dark: #8a8784;
  }
  html, body {
    margin: 0;
    padding: 0;
    width: 1200px;
    height: 1000px;
    overflow: hidden;
    background: var(--page);
  }
  .canvas {
    position: relative;
    width: 1200px;
    height: 1000px;
    background: var(--page);
  }
  .cover {
    position: absolute;
    left: 267px;
    top: 167px;
    width: 666px;
    height: 666px;
    background: var(--board);
  }
  .torn-paper {
    position: absolute;
    left: 0;
    top: 0;
    width: 666px;
    height: 666px;
  }
  .heart {
    position: absolute;
  }
  .heart--right {
    left: 520px;
    top: 135px;
    width: 150px;
    height: 180px;
    transform: rotate(-28deg);
  }
  .heart--left {
    left: 5px;
    top: 380px;
    width: 155px;
    height: 165px;
    transform: rotate(-42deg);
  }
  .polaroid {
    position: absolute;
    left: 186px;
    top: 89px;
    width: 296px;
    height: 377px;
    margin: 0;
    background: var(--card);
  }
  .polaroid__photo {
    position: absolute;
    left: 18px;
    top: 14px;
    width: 259px;
    height: 259px;
    background: linear-gradient(180deg, var(--photo-light) 0%, var(--photo-dark) 100%);
  }
  .polaroid__caption {
    position: absolute;
    left: 0;
    top: 284px;
    width: 100%;
    margin: 0;
    text-align: center;
    font-family: "Kalam", "Gochi Hand", cursive;
    font-size: 32px;
    line-height: 32px;
    color: var(--ink);
  }
  .tape {
    position: absolute;
    width: 118px;
    height: 50px;
    background: var(--tape);
  }
  .tape--top {
    left: 400px;
    top: 98px;
    transform: rotate(52deg);
  }
  .tape--bottom {
    left: 140px;
    top: 426px;
    transform: rotate(40deg);
  }
  .artist {
    position: absolute;
    left: 0;
    top: 492px;
    width: 666px;
    margin: 0;
    text-align: center;
    font-family: "Gochi Hand", "Kalam", cursive;
    font-weight: 400;
    font-size: 150px;
    line-height: 150px;
    letter-spacing: 6px;
    color: var(--title);
  }
</style>
</head>
<body>
<main class="canvas">
  <section class="cover">
    <svg class="torn-paper" viewBox="0 0 666 666" aria-hidden="true">
      <defs>
        <radialGradient id="paperShade" cx="45%" cy="45%" r="75%">
          <stop offset="0%" stop-color="#444444"/>
          <stop offset="100%" stop-color="#2f2f2f"/>
        </radialGradient>
      </defs>
      <polygon fill="url(#paperShade)" points="
        20,28 40,22 60,26 85,18 110,24 140,20 170,26 200,17 230,22 260,18 290,25 320,19 350,22 380,16 410,23 440,18 470,24 500,19 530,26 560,20 590,24 610,21 655,27
        652,60 657,90 650,120 656,150 649,180 655,210 648,240 654,270 647,300 653,330 646,360 652,390 645,420 651,450 644,480 650,510 643,540 649,570 645,600 650,630 648,650
        620,652 590,648 560,655 530,650 500,656 470,649 440,655 410,650 380,657 350,651 320,656 290,650 260,655 230,649 200,654 170,650 140,656 110,651 80,655 50,649 22,652
        18,620 12,590 17,560 10,530 16,500 9,470 15,440 8,410 14,380 9,350 15,320 10,290 16,260 11,230 17,200 12,170 18,140 13,110 19,80 14,50"/>
    </svg>

    <svg class="heart heart--right" viewBox="0 0 100 100" role="img" aria-label="Orange heart decoration">
      <path fill="var(--heart)" d="M50 90 C20 68 4 50 4 30 C4 14 16 4 29 4 C39 4 46 10 50 18 C54 10 61 4 71 4 C84 4 96 14 96 30 C96 50 80 68 50 90 Z"/>
    </svg>

    <svg class="heart heart--left" viewBox="0 0 100 100" role="img" aria-label="Orange heart decoration">
      <path fill="var(--heart)" d="M50 90 C20 68 4 50 4 30 C4 14 16 4 29 4 C39 4 46 10 50 18 C54 10 61 4 71 4 C84 4 96 14 96 30 C96 50 80 68 50 90 Z"/>
    </svg>

    <figure class="polaroid">
      <div class="polaroid__photo" role="img" aria-label="Photo of two friends sitting together on a bench overlooking a lake"></div>
      <p class="polaroid__caption">Stars over<br>harbour</p>
    </figure>

    <div class="tape tape--top" aria-hidden="true"></div>
    <div class="tape tape--bottom" aria-hidden="true"></div>

    <h1 class="artist">TOVA</h1>
  </section>
</main>
</body>
</html>
```